2020 Lone Ridge Crisis Alliance Conference Event flyer for annual conference held in Amarillo Texas

The Power of Connection

I need a flyer to send out via email. I The flyer will depict our theme, "The Power of Connection" event dates, website and costs. Association is Lone Ridge Crisis Alliance, date April 23-25, 2020, website www.loneridgealliance.org, Early Bird and Member discounts location Harborview Lodge, Amarillo Texas

page 2 will have sponsor info, and keynote description, can be 3 pages if absolutely necessary
: keynote speaker Martin Oakley, Martin is a retired Westbrook Roadway Patrol officer who spent more than 17 years patrolling the Silverfall Span Bridge. During that time he encountered hundreds of people who were troubled and had lost hope. They were ready to jump off the bridge and end their lives. Although a trained negotiator, Oakley also relied on his compassion, gentle voice, eye contact, and his innate ability to “listening to understand”. During his career, he encouraged more than 200 people not to jump, go over the bridge’s rail or come back to solid ground from where they had been standing precariously. These challenging, but rewarding efforts earned him the nickname, “Guardian of the Silverfall Span Bridge”. Retired, Oakley is now dedicating his life to promoting mental health awareness and suicide prevention across the globe.
Great sponsor opportunities available at www.Loneridgealliance.org sponsor letter attached for info on sponsor opportunities it is not necessary to include all info

i attached a mockup page 1 flyer that i really like but graphic designer did not complete this would give you an idea of what i am looking for on page 1 although it is missing a few elements

the Brookhaven (logo attached) is a champion sponsor, Plainsview Visitors Bureau (logo attached)

Target Market(s)

law enforcement, hospitals, mental health providers, court system,

Colors

Designer to choose colors to be used in the design.

Requirements
Must have
• theme -The Power of Connection
• website
• dates
• location
• costs
Nice to have
• prefer graphic related to theme
• Brookhaven is a large sponsor
• need to have 2-3 pages for all info
• include info on sponsor opportunities but does not have to include all info on attachment

```html
<!DOCTYPE html>
<html lang="en">
<head>
<meta charset="utf-8">
<title>The Power of Connection — Lone Ridge Crisis Alliance Conference 2020</title>
<link rel="stylesheet" href="https://fonts.googleapis.com/css2?family=Great+Vibes&family=Open+Sans:wght@400;600;700&family=Playfair+Display:wght@400;700;900&display=swap">
<style>
  :root {
    --backdrop: #7f5d12;
    --paper: #ffffff;
    --ink: #23282d;
    --orange: #f3a93a;
    --slate: #3d4b57;
    --slate-dark: #2e3a44;
    --slate-light: #5a6874;
    --mist: #c6c9cc;
    --mist-light: #dfe2e4;
    --photo-dark: #1f1a14;
    --photo-warm: #b88a45;
    --partner-green: #2f7a3c;
    --partner-blue: #2a4a9a;
  }
  * { box-sizing: border-box; margin: 0; padding: 0; }
  html, body { width: 1200px; height: 840px; overflow: hidden; }
  body { background: var(--backdrop); position: relative; font-family: "Open Sans", Arial, sans-serif; }

  .page { position: absolute; top: 76px; width: 538px; height: 682px; overflow: hidden; }
  .page--cover { left: 50px; background: var(--paper); }
  .page--sponsors { left: 626px; background: var(--mist); }

  /* Cover */
  .cover-photo { position: absolute; left: 0; top: 0; width: 538px; height: 330px; }
  .cover-title { position: absolute; left: 0; top: 284px; width: 100%; font-family: "Playfair Display", Georgia, serif; }
  .title-the { position: absolute; left: 26px; top: 4px; font-size: 64px; font-weight: 900; color: var(--ink); letter-spacing: 1px; }
  .title-power { position: absolute; left: 112px; top: 49px; font-size: 74px; font-weight: 700; color: var(--orange); letter-spacing: 1px; white-space: nowrap; }
  .title-connection { position: absolute; left: 136px; top: 107px; font-family: "Great Vibes", cursive; font-size: 92px; color: var(--ink); line-height: 1; }
  .cover-org { position: absolute; left: 0; top: 474px; width: 100%; text-align: center; font-family: "Playfair Display", Georgia, serif; font-weight: 700; font-size: 17px; color: var(--ink); letter-spacing: 0.5px; }
  .cover-year { position: absolute; left: 0; top: 488px; width: 100%; text-align: center; font-family: "Great Vibes", cursive; font-size: 72px; color: var(--ink); }
  .cover-dates { position: absolute; left: 0; top: 557px; width: 100%; text-align: center; font-family: "Playfair Display", Georgia, serif; font-size: 23px; color: var(--orange); }
  .cover-location { position: absolute; left: 0; top: 597px; width: 100%; text-align: center; font-family: "Playfair Display", Georgia, serif; font-weight: 700; font-size: 14px; color: var(--orange); letter-spacing: 0.5px; }

  .partner-row { position: absolute; left: 0; top: 636px; width: 100%; height: 20px; display: flex; justify-content: space-around; align-items: center; padding: 0 40px; }
  .partner { display: flex; align-items: center; gap: 5px; font-family: "Open Sans", Arial, sans-serif; font-weight: 700; font-size: 9.5px; color: var(--ink); white-space: nowrap; }
  .partner-mark { display: inline-block; width: 14px; height: 14px; }
  .partner-mark--square { background: var(--partner-green); }
  .partner-mark--circle { border-radius: 50%; background: var(--partner-blue); }

  /* Sponsors */
  .backdrop-shape { position: absolute; left: 0; top: 0; width: 538px; height: 682px; }
  .champion { position: absolute; left: 115px; top: 42px; width: 310px; height: 172px; background: var(--slate); color: #fff; padding: 40px 16px 8px 30px; }
  .champion-title { position: absolute; left: 60px; top: -22px; width: 190px; height: 44px; background: var(--slate-dark); border: 2px solid var(--slate-light); color: #fff; font-family: "Playfair Display", Georgia, serif; font-size: 15px; letter-spacing: 1px; display: flex; align-items: center; justify-content: center; }
  .champion-list { list-style: none; font-size: 8.8px; line-height: 1.22; }
  .champion-list li::before { content: "* "; }
  .champion-list .indent { padding-left: 7px; }
  .champion-list .indent::before { content: ""; }

  .tier-band { position: absolute; left: 0; top: 248px; width: 538px; height: 30px; background: var(--slate); }
  .tiers { position: absolute; left: 19px; top: 248px; width: 501px; display: flex; gap: 3px; }
  .tier { flex: 1; display: flex; flex-direction: column; height: 222px; }
  .tier-price { height: 24px; background: var(--slate); color: #fff; font-family: "Playfair Display", Georgia, serif; font-size: 9.5px; display: flex; align-items: center; justify-content: center; }
  .tier-role { height: 40px; background: var(--mist-light); color: var(--ink); font-family: "Playfair Display", Georgia, serif; font-size: 9.5px; line-height: 1.2; text-align: center; display: flex; align-items: center; justify-content: center; padding: 0 6px; }
  .tier-perks { flex: 1; background: var(--paper); border-radius: 0 0 10px 10px; list-style: none; padding: 6px 5px 6px 7px; font-size: 7.6px; line-height: 1.2; color: var(--ink); }

  .addons { position: absolute; left: 26px; top: 493px; width: 490px; display: flex; gap: 12px; }
  .addon { flex: 1; height: 104px; background: var(--slate-light); color: #fff; display: flex; flex-direction: column; }
  .addon-head { height: 36px; background: var(--slate); font-family: "Playfair Display", Georgia, serif; font-size: 9px; line-height: 1.2; letter-spacing: 0.4px; display: flex; align-items: center; justify-content: center; text-align: center; padding: 0 4px; }
  .addon-body { padding: 6px 7px; font-size: 7.6px; line-height: 1.25; text-align: center; }

  .register { position: absolute; left: 0; top: 607px; width: 538px; height: 75px; background: var(--orange); color: #fff; font-family: "Playfair Display", Georgia, serif; font-weight: 700; font-size: 19px; line-height: 1.25; letter-spacing: 1px; text-align: center; display: flex; flex-direction: column; justify-content: center; }
  .register-url { font-size: 15px; }
</style>
</head>
<body>

<section class="page page--cover" aria-label="Conference cover">
  <svg class="cover-photo" viewBox="0 0 538 330" role="img" aria-label="Photo of a small lightbulb-headed wire figure plugging a cord into a wall socket, warm light on a dark wall">
    <defs>
      <radialGradient id="photoGlow" cx="0.48" cy="0.42" r="0.7">
        <stop offset="0" stop-color="#b88a45"/>
        <stop offset="0.55" stop-color="#5d4628"/>
        <stop offset="1" stop-color="#1f1a14"/>
      </radialGradient>
    </defs>
    <path d="M0 0 H538 V60 A300 300 0 0 1 270 330 A300 300 0 0 1 0 60 Z" fill="url(#photoGlow)"/>
  </svg>

  <h1 class="cover-title">
    <span class="title-the">THE</span>
    <span class="title-power">POWER OF</span>
    <span class="title-connection">Connection</span>
  </h1>
  <p class="cover-org">LONE RIDGE CRISIS ALLIANCE CONFERENCE</p>
  <p class="cover-year">2020</p>
  <p class="cover-dates">APRIL 23-25, 2020</p>
  <p class="cover-location">AMARILLO TEXAS</p>

  <div class="partner-row">
    <span class="partner">Plainsview Visitors Bureau</span>
    <span class="partner"><span class="partner-mark partner-mark--square"></span>The Brookhaven</span>
    <span class="partner"><span class="partner-mark partner-mark--circle"></span>Lone Ridge Crisis Alliance</span>
  </div>
</section>

<section class="page page--sponsors" aria-label="Sponsor opportunities">
  <svg class="backdrop-shape" viewBox="0 0 538 682" aria-hidden="true">
    <rect x="0" y="0" width="538" height="96" fill="#f3a93a"/>
    <circle cx="269" cy="250" r="262" fill="#f3a93a"/>
  </svg>

  <div class="champion">
    <h2 class="champion-title">CHAMPION $10,000</h2>
    <ul class="champion-list">
      <li>Conference Sponsor</li>
      <li>Opportunity to Introduce Speaker</li>
      <li>Lone Ridge Crisis Alliance 2020 Conference</li>
      <li class="indent">Presented by "your organization"</li>
      <li class="indent">on front cover</li>
      <li>Full Page Program Ad</li>
      <li>Acknowledgments in Media Spotlight</li>
      <li>Personal Signage (color)</li>
      <li>Exhibit Booth</li>
      <li>10 Paid Registrations</li>
      <li>Sponsor Ribbons (10)</li>
      <li>Organizational Membership Lone Ridge</li>
    </ul>
  </div>

  <div class="tier-band"></div>
  <div class="tiers">
    <article class="tier">
      <h3 class="tier-price">Visionary $8,000</h3>
      <p class="tier-role">Award Luncheon Sponsor</p>
      <ul class="tier-perks">
        <li>*Includes Opportunity to Introduce Speaker</li>
        <li>*Full Page Program Ad</li>
        <li>*Acknowledgments in Media Spotlights</li>
        <li>*Personalized Signage (Color)</li>
        <li>*Exhibit Booth</li>
        <li>*8 paid Registrations</li>
        <li>*Sponsor Ribbons (8)</li>
        <li>*Organizational Membership Lone Ridge</li>
      </ul>
    </article>
    <article class="tier">
      <h3 class="tier-price">Leader $5,000</h3>
      <p class="tier-role">Morning Plenary Sponsor</p>
      <ul class="tier-perks">
        <li>*Includes Opportunity to Introduce Speaker</li>
        <li>*Full Page Program Ad</li>
        <li>*Acknowledgments in Media Spotlights</li>
        <li>*Personalized Signage (Color)</li>
        <li>*Exhibit Booth</li>
        <li>*5 paid Registrations</li>
        <li>*Sponsor Ribbons (5)</li>
        <li>*Organizational Membership Lone Ridge</li>
      </ul>
    </article>
    <article class="tier">
      <h3 class="tier-price">Builder $2,500</h3>
      <p class="tier-role">Workshop Sponsor</p>
      <ul class="tier-perks">
        <li>*Includes Opportunity to Introduce Speaker</li>
        <li>*Half Page Program Ad</li>
        <li>*Acknowledgments in Media Spotlights</li>
        <li>*Group Signage (Color)</li>
        <li>*Exhibit Booth</li>
        <li>*3 paid Registrations</li>
        <li>*Sponsor Ribbons (3)</li>
        <li>*Organizational Membership Lone Ridge</li>
      </ul>
    </article>
    <article class="tier">
      <h3 class="tier-price">Advocate $1,000</h3>
      <p class="tier-role">Workshop Sponsor</p>
      <ul class="tier-perks">
        <li>*Includes Opportunity to Introduce Speaker</li>
        <li>*Half Page Program Ad</li>
        <li>*Acknowledgments in Media Spotlights</li>
        <li>*Group Signage (Color)</li>
        <li>*Exhibit Booth</li>
        <li>*2 paid Registrations</li>
        <li>*Sponsor Ribbons (2)</li>
        <li>*Organizational Membership Lone Ridge</li>
      </ul>
    </article>
    <article class="tier">
      <h3 class="tier-price">Friend $500</h3>
      <p class="tier-role">Workshop Sponsor</p>
      <ul class="tier-perks">
        <li>*Company Logo</li>
        <li>*Exhibit Booth</li>
        <li>*1 Paid Registration</li>
        <li>*Sponsor Ribbon(1)</li>
        <li>*Organizational Membership to Lone Ridge</li>
      </ul>
    </article>
  </div>

  <div class="addons">
    <article class="addon">
      <h3 class="addon-head">SPONSOR AN OFFICER $500</h3>
      <p class="addon-body">*Covers conference training for one officer. *Company Logo and recognition in Print material</p>
    </article>
    <article class="addon">
      <h3 class="addon-head">EXHIBITOR $250</h3>
      <p class="addon-body">*Exhibit Booth</p>
    </article>
    <article class="addon">
      <h3 class="addon-head">Coin Sponsor $1000 (only 1) add-on to another package</h3>
      <p class="addon-body">Conference Coin will be designed for giveaway w/ sponsor logo on the back.</p>
    </article>
    <article class="addon">
      <h3 class="addon-head">Program ADS</h3>
      <p class="addon-body">*$250 1/4 page ad<br>*$500 1/2 page ad<br>*$1000 full page ad</p>
    </article>
  </div>

  <footer class="register">
    <span>REGISTER AT</span>
    <span class="register-url">WWW.LONERIDGEALLIANCE.ORG</span>
  </footer>
</section>

</body>
</html>
```